Figure for a research paper

I am working on designing a figure for a research paper that illustrates the effect of KADO Pathways assessment on student outcomes over time by impacting teacher bias and teacher perception of student growth. I built the attached figure via powerpoint. It includes the very basic elements but it does not look great and I am not sure that it is clearly depicting what I am hoping to illustrate. I would like for you to build an illustration of this idea that i can include in the paper.

```html
<!DOCTYPE html>
<html lang="en">
<head>
<meta charset="utf-8">
<title>KADO Pathways Assessment and Student Outcomes Over Time</title>
<link href="https://fonts.googleapis.com/css2?family=Montserrat:wght@500;600;700;800&display=swap" rel="stylesheet">
<style>
  :root {
    --bg: #ffffff;
    --ink: #2b2b2b;
    --ink-soft: #4a4a4a;
    --axis-y: #f5a21b;
    --axis-x: #1fb58a;
    --assessment: #ef5f7d;
    --assessment-tint: #fde6ec;
    --baseline: #9fb2e2;
    --alert: #f06a3a;
    --head-top: #c9daf0;
    --head-bottom: #a3bfe4;
    --guide: #b9b9b9;
  }
  * { margin: 0; padding: 0; box-sizing: border-box; }
  html, body { width: 1200px; height: 1200px; overflow: hidden; background: var(--bg); }
  .figure {
    position: relative;
    width: 1200px;
    height: 1200px;
    font-family: "Montserrat", sans-serif;
    color: var(--ink);
  }
  .chart { position: absolute; inset: 0; }

  .student-icon {
    position: absolute;
    left: 68px;
    top: 392px;
    width: 148px;
    height: 140px;
    border-radius: 16px;
    background: linear-gradient(180deg, #f6e6ea 0%, #dfeaf7 58%, #8fc1ef 100%);
  }
  .y-label {
    position: absolute;
    left: 20px;
    top: 548px;
    width: 244px;
    text-align: center;
    font-weight: 700;
    font-size: 23px;
    line-height: 1.3;
  }

  .head-icon {
    position: absolute;
    top: 558px;
    width: 88px;
    height: 84px;
    border-radius: 44px 44px 18px 34px;
    background: linear-gradient(165deg, var(--head-top) 0%, var(--head-bottom) 100%);
  }
  .head-icon.bias { left: 726px; }
  .head-icon.perception { left: 834px; }

  .note {
    position: absolute;
    font-weight: 700;
    font-size: 16px;
    line-height: 1.3;
    color: var(--ink-soft);
  }
  .note.bias { left: 644px; top: 632px; width: 100px; text-align: center; }
  .note.perception { left: 940px; top: 550px; width: 200px; }

  .time-label {
    position: absolute;
    left: 548px;
    top: 842px;
    width: 320px;
    text-align: center;
    font-weight: 800;
    font-size: 40px;
    letter-spacing: 10px;
    color: var(--axis-x);
  }
</style>
</head>
<body>
<div class="figure">
  <svg class="chart" width="1200" height="1200" viewBox="0 0 1200 1200" xmlns="http://www.w3.org/2000/svg">
    <defs>
      <linearGradient id="gap-fill" x1="0" y1="0" x2="1" y2="0">
        <stop offset="0" stop-color="var(--assessment-tint)" stop-opacity="0"/>
        <stop offset="1" stop-color="var(--assessment-tint)" stop-opacity="1"/>
      </linearGradient>
    </defs>

    <!-- gap between assessed growth and perceived growth -->
    <polygon class="growth-gap" points="290,730 1050,400 1075,655 290,735" fill="url(#gap-fill)"/>

    <!-- axes -->
    <g class="axes" stroke-width="5" stroke-linecap="round">
      <line x1="276" y1="312" x2="276" y2="820" stroke="var(--axis-y)"/>
      <polygon points="276,292 265,316 287,316" fill="var(--axis-y)" stroke="none"/>
      <line x1="276" y1="820" x2="1118" y2="820" stroke="var(--axis-x)"/>
      <polygon points="1138,820 1114,809 1114,831" fill="var(--axis-x)" stroke="none"/>
    </g>

    <!-- trend lines -->
    <line class="trend-assessment" x1="290" y1="725" x2="1050" y2="400" stroke="var(--assessment)" stroke-width="6" stroke-linecap="round"/>
    <line class="trend-perceived" x1="290" y1="735" x2="1075" y2="655" stroke="var(--baseline)" stroke-width="6" stroke-linecap="round"/>
    <circle cx="1050" cy="400" r="7" fill="var(--assessment)"/>
    <circle cx="1075" cy="655" r="7" fill="var(--baseline)"/>

    <text class="line-label" transform="translate(440 643) rotate(-23.15)"
          font-family="Montserrat, sans-serif" font-weight="700" font-size="28" fill="var(--assessment)">KADO Pathways Framework Assessment</text>

    <!-- teacher bias guide -->
    <line x1="694" y1="678" x2="694" y2="750" stroke="var(--guide)" stroke-width="1.5" stroke-dasharray="4 4"/>

    <!-- downward influence arrows -->
    <g class="influence-arrow" fill="var(--alert)">
      <rect x="765.5" y="644" width="9" height="22" rx="2"/>
      <polygon points="756,662 784,662 770,684"/>
      <rect x="873.5" y="644" width="9" height="12" rx="2"/>
      <polygon points="864,652 892,652 878,673"/>
    </g>

    <!-- clock -->
    <g class="clock-icon" fill="none" stroke="var(--axis-x)" stroke-width="4" stroke-linecap="round">
      <circle cx="1091" cy="772" r="23"/>
      <path d="M1091 760 V773 H1101"/>
      <path d="M1069 749 a12 12 0 0 1 14 -6"/>
      <path d="M1113 749 a12 12 0 0 0 -14 -6"/>
      <line x1="1076" y1="794" x2="1071" y2="800"/>
      <line x1="1106" y1="794" x2="1111" y2="800"/>
    </g>
  </svg>

  <div class="student-icon" role="img" aria-label="Icon of a student connected to three assessment checklists"></div>
  <p class="y-label">Effectiveness<br>of KADO Pathways<br>Program on<br>the Student</p>

  <div class="head-icon bias" role="img" aria-label="Head profile with a lightbulb, representing teacher bias"></div>
  <div class="head-icon perception" role="img" aria-label="Head profile with a growing plant, representing perception of student growth"></div>

  <p class="note bias">Teacher<br>Bias</p>
  <p class="note perception">Teacher's inaccurate perception of student growth (or learning)</p>

  <p class="time-label">TIME</p>
</div>
</body>
</html>
```